Book cover design about quality management systems

Book cover design that I can display in my website for ore orders
The book is about helping organisations to fully integrate their Quality management systems rather than having a quality system which sits off to the side and adds extra work.
It is aimed at organisations leaders
It is about leaders taking ownership and leading the decision and design of the quality management system and therefore being able to delegate more effectively.

Target Market(s)

CEO of government funded organisations

Industry/Entity Type

Management

Font styles to use
Sans Serif

Colors

Designer to choose colors to be used in the design.

Requirements
Must have
• Ability to be used on website
• Title of the book
• Anchor lantern harvest
• Strap line - Turning standards into results
Nice to have
• Not too fussy
• Not a black cover
• Deep Yellow in the design if possible
Should not have
• Anything too feminine

```html
<!DOCTYPE html>
<html lang="en">
<head>
<meta charset="utf-8">
<title>Anchor Lantern Harvest – Book Cover</title>
<link rel="stylesheet" href="https://fonts.googleapis.com/css2?family=Teko:wght@400;500&family=Saira+Semi+Condensed:wght@500;600&family=EB+Garamond&display=swap">
<style>
  :root {
    --page-bg: #eeeeee;
    --cover-white: #ffffff;
    --ink: #111111;
    --deep-yellow: #d8ae00;
    --gold-soft: #efe6cf;
    --body-ink: #2a2a2a;
  }
  * { margin: 0; padding: 0; box-sizing: border-box; }
  html, body { width: 1200px; height: 800px; overflow: hidden; }
  body {
    background: var(--page-bg);
    position: relative;
  }
  .cover-wrap {
    position: absolute;
    left: 222px; top: 140px;
    width: 756px; height: 520px;
    display: flex;
    box-shadow: 0 6px 24px rgba(0,0,0,0.12);
  }
  .back-cover, .front-cover {
    width: 360px; height: 520px;
    background: var(--cover-white);
    position: relative;
    overflow: hidden;
  }
  .spine {
    width: 36px; height: 520px;
    background: var(--deep-yellow);
    position: relative;
  }
  .spine-text {
    position: absolute;
    left: 50%; top: 18px;
    transform: translateX(-50%);
    writing-mode: vertical-rl;
    display: flex; align-items: center;
  }
  .spine-title {
    font-family: "Teko", sans-serif;
    font-weight: 500;
    font-size: 24px;
    letter-spacing: 0.5px;
    color: var(--ink);
    text-transform: uppercase;
    line-height: 1;
  }
  .spine-author {
    margin-top: 24px;
    font-family: "Saira Semi Condensed", sans-serif;
    font-weight: 500;
    font-size: 8px;
    letter-spacing: 3px;
    color: var(--ink);
    text-transform: uppercase;
  }
  .book-title {
    position: absolute;
    left: 22px; top: 18px;
    font-family: "Teko", sans-serif;
    font-weight: 500;
    font-size: 74px;
    line-height: 0.82;
    color: var(--ink);
    text-transform: uppercase;
    z-index: 1;
  }
  .strapline {
    position: absolute;
    left: 22px; top: 206px;
    font-family: "Teko", sans-serif;
    font-weight: 400;
    font-size: 29px;
    line-height: 1;
    color: var(--ink);
    text-transform: uppercase;
    white-space: nowrap;
    z-index: 1;
  }
  .author-name {
    position: absolute;
    left: 0; right: 0; top: 458px;
    text-align: center;
    font-family: "Saira Semi Condensed", sans-serif;
    font-weight: 600;
    font-size: 23px;
    letter-spacing: 8px;
    color: var(--ink);
    text-transform: uppercase;
    z-index: 1;
  }
  .network-art {
    position: absolute;
    background: radial-gradient(ellipse at center, var(--gold-soft) 0%, rgba(239,230,207,0.4) 55%, rgba(255,255,255,0) 75%);
  }
  .network-art--top { left: 190px; top: 0; width: 170px; height: 160px; }
  .network-art--middle { left: 60px; top: 260px; width: 300px; height: 180px; }
  .network-art--back { left: 0; top: 300px; width: 360px; height: 220px; }
  .blurb {
    position: absolute;
    left: 14px; right: 24px; top: 22px;
    font-family: "EB Garamond", serif;
    font-size: 8.6px;
    line-height: 1.4;
    color: var(--body-ink);
    text-align: justify;
    hyphens: auto;
  }
  .blurb p + p { margin-top: 9px; }
</style>
</head>
<body>
  <div class="cover-wrap">
    <section class="back-cover">
      <div class="blurb">
        <p>Lorem ipsum dolor sit amet, consectetur adipiscing elit. Curabitur porta mi vitae finibus porttitor. Aenean congue ultrices neque et dapibus. Phasellus at massa vel ligula consequat tincidunt vel in orci. Quisque posuere, nibh laoreet sollicitudin blandit, diam sem pretium mi, id venenatis nisi erat non ipsum. Vivamus bibendum sit amet sem at ullamcorper. Duis congue, mi in placerat vulputate, nisl neque rhoncus ipsum, sed ullamcorper leo nisl at urna. Nulla finibus nisi non magna ultrices, in dignissim velit ultrices. Phasellus venenatis elementum augue non lobortis. Praesent blandit felis arcu. Pellentesque auctor, lectus ac ultrices vulputate, leo nisi viverra nisi, quis volutpat sapien massa vel odio. Orci varius natoque penatibus et magnis dis parturient montes, nascetur ridiculus mus. Phasellus vel dictum mauris. Sed tristique tellus vitae tortor aliquam luctus quis non felis. Vivamus laoreet, ipsum ac aliquet efficitur, libero nunc aliquet ipsum, facilisis consectetur nunc est vitae ipsum.</p>
        <p>Phasellus pellentesque elementum porta. Sed eget sem ante. Quisque tincidunt lorem id pretium pretium. Nulla ut lectus pharetra, congue metus vel, sagittis augue. Nulla eget sollicitudin risus, gravida eleifend turpis. Nulla hendrerit metus eget mauris placerat, vitae aliquet justo tincidunt. Aenean arcu tellus, eleifend sit amet enim finibus, facilisis fringilla lectus. Sed viverra fringilla sem, nec eleifend quam ornare ut. Sed et mauris maximus, porttitor lacus at, congue eros. Interdum et malesuada fames ac ante ipsum primis in faucibus. Ut pulvinar libero augue, at commodo arcu rutrum non.</p>
      </div>
      <div class="network-art network-art--back" role="img" aria-label="Gold connected-dots network pattern"></div>
    </section>

    <section class="spine">
      <div class="spine-text">
        <span class="spine-title">Anchor Lantern Harvest</span>
        <span class="spine-author">Helena Marsh</span>
      </div>
    </section>

    <section class="front-cover">
      <div class="network-art network-art--top" role="img" aria-label="Gold connected-dots network pattern"></div>
      <div class="network-art network-art--middle" role="img" aria-label="Gold connected-dots network pattern"></div>
      <h1 class="book-title">Anchor<br>Lantern<br>Harvest</h1>
      <p class="strapline">Turning standards into results</p>
      <p class="author-name">Helena Marsh</p>
    </section>
  </div>
</body>
</html>
```